Software engineering company needs business card

I need a cool business card. Company: Soft Belan Brindlewood Ave 41 58207 Sincity Name: Gerald Vanholt CEO / Managing Director & Owner

```html
<!DOCTYPE html>
<html lang="de">
<head>
<meta charset="utf-8">
<title>Soft Belan – Visitenkarte</title>
<link href="https://fonts.googleapis.com/css2?family=Lato:wght@300;400;700&display=swap" rel="stylesheet">
<style>
  :root {
    --stage: #e9e7e3;
    --card-light: #f1f1ef;
    --card-dark: #232323;
    --ink: #2b2b2b;
    --ink-soft: #555555;
    --accent: #7cc242;
    --mark-grey: #8a8a8a;
  }
  * { margin: 0; padding: 0; box-sizing: border-box; }
  html, body {
    width: 1200px;
    height: 848px;
    overflow: hidden;
    background: var(--stage);
    font-family: "Lato", sans-serif;
  }
  .stage {
    width: 1200px;
    height: 848px;
    display: flex;
    align-items: center;
    justify-content: center;
    gap: 40px;
  }
  .card {
    width: 540px;
    height: 309px;
    border-radius: 22px;
    position: relative;
    box-shadow: 0 8px 24px rgba(0,0,0,0.18);
  }
  .card--front { background: var(--card-light); color: var(--ink); }
  .card--back {
    background: var(--card-dark);
    display: flex;
    align-items: center;
    justify-content: center;
  }
  .front-brand {
    position: absolute;
    left: 44px;
    top: 170px;
    display: flex;
    align-items: center;
    gap: 10px;
  }
  .front-brand__dot {
    width: 14px;
    height: 14px;
    background: var(--accent);
  }
  .front-brand__name {
    font-weight: 700;
    font-size: 26px;
    color: var(--mark-grey);
    letter-spacing: 1px;
  }
  .contact {
    position: absolute;
    left: 270px;
    top: 52px;
  }
  .contact__name {
    font-size: 22px;
    font-weight: 300;
    color: var(--ink);
  }
  .contact__name strong { font-weight: 700; }
  .contact__role {
    font-size: 13px;
    color: var(--accent);
    margin-top: 2px;
  }
  .contact__list {
    list-style: none;
    margin-top: 22px;
    font-size: 13px;
    color: var(--ink-soft);
    line-height: 1.35;
  }
  .contact__list li {
    display: flex;
    align-items: flex-start;
    gap: 12px;
    margin-bottom: 12px;
  }
  .contact__icon {
    width: 13px;
    height: 13px;
    flex: none;
    margin-top: 2px;
    fill: var(--accent);
  }
  .back-brand {
    font-weight: 700;
    font-size: 44px;
    letter-spacing: 6px;
    color: var(--accent);
  }
</style>
</head>
<body>
<main class="stage">
  <section class="card card--front" aria-label="Vorderseite">
    <div class="front-brand">
      <span class="front-brand__dot"></span>
      <span class="front-brand__name">Soft Belan</span>
    </div>
    <div class="contact">
      <p class="contact__name">Gerald <strong>Vanholt</strong></p>
      <p class="contact__role">CEO / Geschäftsführer &amp; Inhaber</p>
      <ul class="contact__list">
        <li>
          <svg class="contact__icon" viewBox="0 0 12 12" aria-hidden="true"><path d="M6 0a4 4 0 0 0-4 4c0 3 4 8 4 8s4-5 4-8a4 4 0 0 0-4-4zm0 5.5A1.5 1.5 0 1 1 6 2.5a1.5 1.5 0 0 1 0 3z"/></svg>
          <span>Brindlewood Ave 41<br>58207 Sincity</span>
        </li>
        <li>
          <svg class="contact__icon" viewBox="0 0 12 12" aria-hidden="true"><path d="M1 4c0-1 1-2 2-2h6c1 0 2 1 2 2v1H8V4H4v1H1zm1 2h8l1 5H1zm4 1a1.5 1.5 0 1 0 0 3 1.5 1.5 0 0 0 0-3z"/></svg>
          <span>000 000 0000</span>
        </li>
        <li>
          <svg class="contact__icon" viewBox="0 0 12 12" aria-hidden="true"><path d="M0 2h12v1L6 7 0 3zm0 2.2 6 4 6-4V10H0z"/></svg>
          <span>youremail@xyz.com</span>
        </li>
      </ul>
    </div>
  </section>
  <section class="card card--back" aria-label="Rückseite">
    <p class="back-brand">SOFT BELAN</p>
  </section>
</main>
</body>
</html>
```